Brontaro Web Site

Redesigned web site for Brontaro Ltd (www.brontaro-example.co.uk). This is to feature new logo (attached). Brontaro Ltd is a company which specialises in Geographic Information Systems and Geographic data - we call ourselves GIS Data Specialists. We are looking for something which conveys our professionalism and our experience. There will be more pages than on the current Brontaro website. There will be: Home, Data Migration, Data Cleansing & Validation, Data Analysis, Data Maintenance, Data Quality and an About Us page. All these should be accessible from each page on the website.
Updates
I didn't really think to say that the content of the web site is going to change from the current one we have. There will be more pages than on the current one. They will be: Home, Data Migration, Data Cleansing & Validation, Data Analysis, Data Maintenance, Data Quality and an About Us page. All these should be accessible from each page on the website. I didn't really think through the fact that the number of pages / areas to access can influence the layout of the site, sorry.
Target Market(s)
Utility Companies (e.g. telecommunications providers, energy companies), local government.
Industry/Entity Type
It Company
Look and feel

```html
<!DOCTYPE html>
<html lang="en">
<head>
<meta charset="utf-8">
<title>Brontaro – GIS Data Specialists</title>
<link rel="stylesheet" href="https://fonts.googleapis.com/css2?family=Arimo:wght@400;700&family=Ubuntu:wght@500&display=swap">
<style>
  :root {
    --page-bg: #454242;
    --nav-green: #b6d04a;
    --nav-rule: #8da336;
    --nav-text: #262626;
    --ribbon-orange: #d99a0f;
    --ribbon-black: #111111;
    --ribbon-green: #6fc51c;
    --card-green: #86993f;
    --card-orange: #d39500;
    --card-black: #000000;
    --white: #ffffff;
    --muted: #8b8888;
  }
  * { margin: 0; padding: 0; box-sizing: border-box; }
  html, body { width: 1200px; height: 1030px; overflow: hidden; }
  body {
    background: var(--page-bg);
    font-family: "Arimo", Arial, sans-serif;
    color: var(--white);
    position: relative;
  }
  .brand {
    position: absolute; left: 150px; top: 58px;
    display: flex; align-items: center; gap: 12px;
  }
  .brand-dot { width: 44px; height: 44px; border-radius: 50%; background: var(--white); }
  .brand-name { font-size: 38px; font-weight: 700; color: var(--white); letter-spacing: -0.5px; }

  .contact {
    position: absolute; right: 135px; top: 30px;
    list-style: none; text-align: right; font-size: 13px; line-height: 20px;
  }
  .contact li { display: flex; justify-content: flex-end; align-items: center; gap: 8px; }
  .contact svg { width: 16px; height: 14px; }

  .frames { position: absolute; left: 0; top: 0; }

  .main-nav {
    position: absolute; left: 158px; top: 178px; width: 234px;
    list-style: none;
  }
  .main-nav li {
    height: 32px; border-bottom: 1px solid var(--nav-rule);
    margin-left: 12px; position: relative;
    font-size: 16.5px; line-height: 32px; color: var(--nav-text);
  }
  .main-nav li::before {
    content: ""; position: absolute; left: -12px; top: 11px;
    border-left: 5px solid #111; border-top: 4px solid transparent; border-bottom: 4px solid transparent;
  }

  .hero-photo {
    position: absolute; left: 424px; top: 104px; width: 648px; height: 333px;
    background: radial-gradient(ellipse at 40% 45%, #9a9a9a 0%, #7b7b7b 45%, #5f5f5f 100%);
  }
  .hero-note {
    position: absolute; left: 888px; top: 128px; width: 165px;
    font-size: 12px; line-height: 15px; text-align: center; color: #f2f2f2;
  }
  .ribbon {
    position: absolute; left: 830px; width: 258px; height: 40px;
    font-family: "Ubuntu", Tahoma, sans-serif; font-weight: 500; font-size: 17px;
    line-height: 40px; padding-left: 26px; color: var(--white);
    clip-path: polygon(14px 0, 100% 0, 100% 100%, 14px 100%, 0 50%);
  }
  .ribbon-orange { top: 184px; background: linear-gradient(#e6ad22, var(--ribbon-orange)); }
  .ribbon-black { top: 239px; background: var(--ribbon-black); padding-left: 23px; }
  .ribbon-green { top: 294px; background: linear-gradient(#86d92e, var(--ribbon-green)); }

  .content-panel {
    position: absolute; left: 150px; top: 470px; width: 900px; height: 448px;
    background: linear-gradient(90deg, #464343, #4f4c4c 20%, #4f4c4c 80%, #464343);
    border-top: 1px solid #555151;
  }
  .welcome-title { position: absolute; left: 36px; top: 28px; font-size: 26px; font-weight: 400; }
  .welcome-text { position: absolute; left: 38px; top: 70px; width: 860px; font-size: 16px; line-height: 26px; white-space: nowrap; }

  .card {
    position: absolute; top: 162px; width: 265px; height: 241px;
    border-radius: 20px; padding: 18px 10px 0 17px;
  }
  .card h2 { font-size: 26px; font-weight: 700; margin-bottom: 6px; }
  .card p { font-size: 16px; line-height: 26px; white-space: nowrap; }
  .card .more { position: absolute; right: 15px; bottom: 9px; font-size: 12px; }
  .card-customers { left: 39px; background: var(--card-green); }
  .card-pedigree { left: 318px; background: var(--card-orange); padding-left: 14px; }
  .card-people { left: 597px; background: var(--card-black); padding-left: 14px; }
  .card-people p { padding-left: 2px; }
  .card-people .more { right: 24px; }

  .footer-brand {
    position: absolute; left: 148px; top: 944px;
    display: flex; align-items: center; gap: 7px;
  }
  .footer-brand .brand-dot { width: 22px; height: 22px; background: #a8a6a6; }
  .footer-brand .brand-name { font-size: 19px; color: #a8a6a6; }
  .legal { position: absolute; right: 155px; top: 948px; text-align: right; color: var(--muted); font-size: 13px; }
  .legal-links { font-size: 11px; margin-top: 4px; margin-right: 76px; }
  .legal-links span { margin: 0 8px; }
</style>
</head>
<body>
  <header>
    <div class="brand"><span class="brand-dot"></span><span class="brand-name">Brontaro</span></div>
    <ul class="contact">
      <li><svg viewBox="0 0 16 14"><path d="M3 1c2 0 3 3 2 4l-1 1c1 2 2 3 4 4l1-1c1-1 4 0 4 2 0 2-2 3-4 2C5 12 2 8 1 4 1 2 2 1 3 1z" fill="none" stroke="#fff" stroke-width="1.2"/></svg>+44 (0) 1632 960 418</li>
      <li><svg viewBox="0 0 16 14"><rect x="2" y="5" width="12" height="8" fill="none" stroke="#fff"/><rect x="4" y="1" width="8" height="4" fill="none" stroke="#fff"/><path d="M4 8h8M4 10h8" stroke="#fff"/></svg>+44 (0) 1632 960 419</li>
      <li><svg viewBox="0 0 16 14"><rect x="2" y="3" width="12" height="9" fill="none" stroke="#fff"/><path d="M2 3l6 5 6-5" fill="none" stroke="#fff"/></svg>contact@brontaro-example.co.uk</li>
    </ul>
  </header>

  <svg class="frames" width="1200" height="460" viewBox="0 0 1200 460" aria-hidden="true">
    <polygon points="412,95 1072,95 1083,106 1083,432 1070,446 424,446 412,434" fill="#6b6868"/>
    <polygon points="120,168 134,148 240,148 250,140 412,140 412,446 240,446 230,438 134,438 120,424" fill="#6b6868"/>
    <polygon points="130,176 142,160 236,160 246,152 412,152 412,434 236,434 226,426 142,426 130,412" fill="#b6d04a"/>
  </svg>

  <nav>
    <ul class="main-nav">
      <li>Home</li>
      <li>Data Migration</li>
      <li>Data Cleansing &amp; Validation</li>
      <li>Data Analysis</li>
      <li>Data Maintenance</li>
      <li>Data Quality</li>
      <li>About Us</li>
    </ul>
  </nav>

  <div class="hero-photo" role="img" aria-label="Photo of a businesswoman touching a glowing point on a translucent world map"></div>
  <p class="hero-note">We can be on hand to help with any or all parts of your data projects via: ▾</p>
  <div class="ribbon ribbon-orange">DATA CONSULTANCY</div>
  <div class="ribbon ribbon-black">SOFTWARE DEVELOPMENT</div>
  <div class="ribbon ribbon-green">SYSTEM CONSULTANCY</div>

  <main class="content-panel">
    <h1 class="welcome-title">Welcome to Brontaro</h1>
    <p class="welcome-text">Brontaro was founded in 1994 by a group of geospatial software engineers that recognised the significant value<br>that data, and the systems used to store and analyse this data, could bring to business.</p>

    <section class="card card-customers">
      <h2>Our Customers:</h2>
      <p>We have worked with over 200<br>companies in a myriad of<br>market sectors - from utilities,<br>local and central government,<br>oil and gas, to many spheres of<br>the marine industry.</p>
      <span class="more">read more...</span>
    </section>
    <section class="card card-pedigree">
      <h2>Our Pedigree:</h2>
      <p>We provide a vast bank of knowl-<br>edge and experience to offer an<br>all encompassing service. This<br>ensures that you, as a customer,<br>reap the maximum benefits from<br>your data and systems ...</p>
      <span class="more">read more...</span>
    </section>
    <section class="card card-people">
      <h2>Our People:</h2>
      <p>We have a wide ranging skill set<br>including VANTO 2 qualified<br>Project Managers, fully qualified<br>Software Developers and<br>Experienced Data Consultants.</p>
      <span class="more">read more...</span>
    </section>
  </main>

  <footer>
    <div class="footer-brand"><span class="brand-dot"></span><span class="brand-name">Brontaro</span></div>
    <div class="legal">
      <p>© 2010 Brontaro Ltd. Registered in Scotland No. 480217</p>
      <p class="legal-links">Terms and Conditions<span>|</span>Privacy Policy</p>
    </div>
  </footer>
</body>
</html>
```